GraniteLoop. Customer needs to know about us, what services we provide & contact us

We are a waste tire recycling company. Our primary focus is on providing a sustainable and cost effective service focusing on: Waste Tire Management, Hassle Free Scheduling for Tire Collection, Mobile Shredding & Special site cleanup services. GraniteLoop will be producing TDF, Clean Tire Wire & further materials.
Please look at https://quorvalwheel.example
Please look at https://bandimacorp.example

This is the look and feel of what we want

I have attached a word document with our website info.

Target Market(s)

Tire Install Companies. Such as paltonhaul.example. TDF Purchasers such as kevrofuel.example.

Industry/Entity Type

Waste Tire Recycling

Coding

Coded - Design and coding required

Number of Pages Required

3 page

Font styles to use
Other font styles liked:
• Look at our logo

Requirements
Must have
• We need a 3 page setup for About Us, Services & Contact Us. Contact us should be a form them can fill out and submit to us Images that are related to waste tire recycling. Clean, modern, innovative.
Nice to have
• The color and feel of the website should work with our logo that we did with artmarketly
Should not have
• Anything progressive, political or "woke"

```html
<!DOCTYPE html>
<html lang="en">
<head>
<meta charset="utf-8">
<title>GraniteLoop – Waste Tire Recycling</title>
<link rel="stylesheet" href="https://fonts.googleapis.com/css2?family=Montserrat:wght@500;600;700;800;900&family=Roboto:wght@400;500&display=swap">
<style>
:root{
  --green:#1f9a3e;
  --green-dark:#137a2e;
  --green-light:#2aad4c;
  --ink:#111111;
  --text:#3b3b3b;
  --muted:#6b6b6b;
  --paper:#ffffff;
  --soft:#f3f3f3;
  --dark:#2f322f;
  --black:#050505;
}
*{box-sizing:border-box;margin:0;padding:0}
html,body{width:1200px;height:4910px;overflow:hidden}
body{position:relative;background:var(--paper);font-family:'Roboto',Arial,sans-serif;color:var(--text)}
.section{position:absolute;left:0;width:1200px}
.abs{position:absolute}
.heading{font-family:'Montserrat',sans-serif;font-weight:700;color:var(--ink);text-transform:uppercase;letter-spacing:.5px}
.heading .accent{color:var(--green)}
.btn{position:absolute;display:flex;align-items:center;justify-content:center;font-family:'Montserrat',sans-serif;font-weight:700;font-size:10px;text-transform:uppercase;letter-spacing:.3px;color:#fff;background:var(--green);border-radius:4px 14px 4px 14px}
.body-copy{font-size:12.5px;line-height:1.42;color:var(--text)}
.body-copy p{margin-bottom:14px}

/* header */
.site-header{top:0;height:114px}
.nav-link{position:absolute;top:50px;font-family:'Montserrat',sans-serif;font-weight:700;font-size:13px;color:var(--ink);text-transform:uppercase}
.nav-link.active{color:var(--green)}
.brand{position:absolute;display:flex;align-items:center;gap:8px;font-family:'Montserrat',sans-serif;font-weight:800;color:var(--green)}
.brand .dot{border-radius:50%;background:var(--green)}

/* hero */
.hero{top:114px;height:606px}
.hero-photo{position:absolute;inset:0;background:linear-gradient(160deg,#5a5650 0%,#3b3833 45%,#6e6a60 75%,#8a8272 100%)}
.hero-title{position:absolute;top:190px;width:100%;text-align:center;font-family:'Montserrat',sans-serif;font-weight:800;font-size:88px;color:#fff;letter-spacing:2px}
.hero-curve{position:absolute;left:0;bottom:0}

/* welcome */
.welcome{top:720px;height:671px}
.welcome .heading{position:absolute;top:78px;width:100%;text-align:center;font-size:42px}
.welcome .col{position:absolute;top:190px;width:420px}
.stand{position:absolute;top:497px;width:100%;text-align:center;font-size:21px;color:#333}

/* about */
.about{top:1391px;height:628px;background:linear-gradient(120deg,var(--green-dark),var(--green) 55%,var(--green-light))}
.about .heading{position:absolute;left:152px;top:114px;font-size:42px;color:#fff}
.about .body-copy{position:absolute;left:148px;top:183px;width:436px;color:#fff}
.btn-outline{background:transparent;border:2px solid #fff}
.about-photo{position:absolute;left:632px;top:82px;width:568px;height:485px;border-radius:30px 0 0 0;background:linear-gradient(170deg,#9aa55a 0%,#6b8a3a 35%,#2b3434 60%,#1d2526 80%,#5e7a34 100%)}

/* services */
.services{top:2019px;height:1000px;background:linear-gradient(165deg,#fff 0%,#fff 30%,#f1f1f1 31%,#f4f4f4 100%)}
.services .heading{position:absolute;top:88px;width:100%;text-align:center;font-size:42px}
.card{position:absolute;width:428px;height:282px;background:#fff;box-shadow:0 4px 18px rgba(0,0,0,.09);padding:38px 40px 0 40px}
.card-head{display:flex;align-items:center;gap:18px;margin-bottom:22px}
.card-head h3{font-family:'Montserrat',sans-serif;font-weight:700;font-size:15px;line-height:1.25;color:var(--ink);text-transform:uppercase}
.card p{font-size:10.5px;line-height:1.72;color:var(--muted)}
.card-arrow{position:absolute;right:-1px;bottom:-1px;width:44px;height:38px;border:1.5px solid #222;background:#fff;display:flex;align-items:center;justify-content:center}
.card-arrow.raised{bottom:auto}

/* stats */
.stats{top:3019px;height:334px;background:radial-gradient(ellipse at 50% 50%,#3f433d 0%,#2e312d 60%,#262825 100%)}
.stat{position:absolute;top:90px;width:300px;text-align:center;color:#fff}
.stat strong{display:block;font-family:'Montserrat',sans-serif;font-weight:700;font-size:62px;line-height:1}
.stat span{display:block;margin-top:14px;font-size:14px;line-height:1.3}

/* products */
.products{top:3353px;height:638px}
.products .heading{position:absolute;left:124px;top:150px;font-size:42px}
.products .body-copy{position:absolute;left:124px;top:220px;width:290px;font-size:12.5px;line-height:1.72}
.tile{position:absolute;width:312px;height:212px;border-radius:3px}

/* contact */
.contact{top:3991px;height:581px;background:linear-gradient(180deg,var(--green) 0%,var(--green-dark) 100%)}
.contact .heading{position:absolute;top:102px;width:100%;text-align:center;font-size:42px;color:#fff}
.contact .lead{position:absolute;top:162px;width:100%;text-align:center;font-size:16px;line-height:1.3;color:#fff}
.field{position:absolute;background:#fff;height:38px;padding:10px 10px;font-size:10px;color:#444}
.field.tall{height:84px}
.submit{background:var(--black);border-radius:4px 14px 4px 14px;width:140px;height:32px}

/* footer */
.site-footer{top:4572px;height:338px;background:var(--black);color:#fff}
.footer-brand-box{position:absolute;left:442px;top:13px;width:316px;height:164px;background:#000;border:1px solid #1a1a1a;display:flex;align-items:center;justify-content:center}
.contact-item{position:absolute;top:205px;display:flex;align-items:flex-start;gap:12px;font-size:12px;line-height:1.35}
.contact-item .ico{width:32px;height:32px;border-radius:50%;background:var(--green);display:flex;align-items:center;justify-content:center;flex:none}
.copyright{position:absolute;top:286px;width:100%;text-align:center;font-size:11.5px}
</style>
</head>
<body>

<header class="section site-header">
  <a class="nav-link active" style="left:150px">Home</a>
  <a class="nav-link" style="left:238px">About Us</a>
  <a class="nav-link" style="left:362px">Services</a>
  <div class="brand" style="left:492px;top:36px;font-size:30px">
    <span class="dot" style="width:20px;height:20px"></span>GraniteLoop
  </div>
  <a class="nav-link" style="left:762px">Contact Us</a>
  <div class="btn" style="left:908px;top:41px;width:140px;height:36px">Customer Login</div>
</header>

<section class="section hero">
  <div class="hero-photo" role="img" aria-label="Photo of a tire recycling yard with piles of scrap tires and a loader"></div>
  <h1 class="hero-title">GRANITELOOP</h1>
  <div class="btn" style="left:530px;top:298px;width:140px;height:36px">Contact Us Now</div>
  <svg class="hero-curve" width="1200" height="180" viewBox="0 0 1200 180">
    <path d="M0,60 Q600,200 1200,60 L1200,180 L0,180 Z" fill="#fff"/>
    <path d="M0,78 Q600,212 1200,70" fill="none" stroke="#1f9a3e" stroke-width="9"/>
    <circle cx="586" cy="142" r="17" fill="#1f9a3e" stroke="#fff" stroke-width="3"/>
    <path d="M579,146 a8,8 0 1 1 14,-2" fill="none" stroke="#fff" stroke-width="2"/>
    <path d="M590,140 l4,5 l3,-5" fill="none" stroke="#fff" stroke-width="2"/>
  </svg>
</section>

<section class="section welcome">
  <h2 class="heading">Welcome to <span class="accent">GraniteLoop!</span></h2>
  <div class="col body-copy" style="left:152px">
    <p>GraniteLoop is forging the wat towards a more sustainable future through scrap tire collection &amp; waste tire recycling</p>
    <p>You've got a business to run, and we've got you covered. Let us worry about your scrap tire removal so you don't have to.</p>
    <p>Through the use of innovative technologies, we are not only more eco-friendly but able to pass the savings along to our customers.</p>
    <p>Waste Tire Management is a global problem that GraniteLoop aims to resolve.  Though our innovative approach to waste tire management, we are focused on resolving environmental concerns head-on. All while giving businesses across the region an opportunity to make a difference for the environment and their bottom line.</p>
  </div>
  <div class="col body-copy" style="left:619px">
    <p>Built upon a foundation of innovation, attention to detail, and budget-conscious services, GraniteLoop is at the forefront of pushing the boundaries of what can be achieved through advancing technology. Through our rigorous procedures, environmental commitment we go beyond expectations. GraniteLoop aims to achieve efficiency all while revolutionizing the industry.</p>
    <p>When your company is deciding on used-tire disposal responsibilities you can rest assured that GraniteLoop has your company's interest at its core. Leave the costly equipment, manpower, and output-reducing duties to us. GraniteLoop will help you focus your time where it counts.</p>
    <p>At our heart GraniteLoop's focus is to always better our processes, support our industry, and environment. Here at GraniteLoop we see ourselves as an extension of your team, outdoing competitors on speed, value, and price point.</p>
  </div>
  <p class="stand">Here at GraniteLoop we're making a stand.</p>
  <div class="btn" style="left:510px;top:550px;width:180px;height:36px">Are you joining us</div>
</section>

<section class="section about">
  <h2 class="heading">About Us</h2>
  <div class="body-copy">
    <p>Every Year The EPA estimates that over 300 million scrap tires are generated annually. GraniteLoop is your sustainable business partner that is leading the way forward with a more sustainable eco-friendly approach to the scrap tire industry. Properly reclaiming and recycling these tires into reusable raw materials protects the environment and public health.</p>
    <p>GraniteLoop is committed to sustainability and looking at your waste tires as a means to offer innovation. Let's work together in getting tires out of landfills and bringing awareness to how tires offer access to scarce materials all while creating a greener future for the next generation. We are working towards a better future with a second chance for your waste tires.</p>
  </div>
  <div class="btn btn-outline" style="left:148px;top:460px;width:122px;height:40px">Read More</div>
  <div class="about-photo" role="img" aria-label="Photo of a pile of discarded tires in tall grass"></div>
</section>

<section class="section services">
  <h2 class="heading">Our <span class="accent">Services</span></h2>

  <article class="card" style="left:122px;top:248px">
    <div class="card-head">
      <svg width="44" height="44" viewBox="0 0 44 44"><circle cx="22" cy="22" r="19" fill="none" stroke="#1f9a3e" stroke-width="3"/><circle cx="22" cy="22" r="11" fill="none" stroke="#222" stroke-width="2"/><path d="M16,24 l6,-9 l6,9 z" fill="none" stroke="#1f9a3e" stroke-width="2"/></svg>
      <h3>Waste Tire<br>Management &amp; Recycling</h3>
    </div>
    <p>Our priority is our core focus on providing our clients with industry leading waste tire management services. Here at GraniteLoop we prioritize your that your collection and scheduling is taken care of seamlessly. We are pursuing a different approach to waste tires while taking the burdens off our customers with a priority to responsible tire disposal. GraniteLoop goes the extra mile to be the environmentally friendly used tire disposal handlers in the market.</p>
    <div class="card-arrow"><svg width="18" height="10" viewBox="0 0 18 10"><path d="M0,5 H16 M12,1 L16,5 L12,9" fill="none" stroke="#111" stroke-width="1.8"/></svg></div>
  </article>

  <article class="card" style="left:591px;top:195px;height:282px">
    <div class="card-head">
      <svg width="44" height="44" viewBox="0 0 44 44"><circle cx="22" cy="22" r="14" fill="none" stroke="#1f9a3e" stroke-width="3"/><path d="M16,16 l12,12 M28,16 l-12,12" stroke="#1f9a3e" stroke-width="2"/><path d="M4,12 a20,20 0 0 1 10,-8 M40,32 a20,20 0 0 1 -10,8" fill="none" stroke="#222" stroke-width="2"/></svg>
      <h3>Tire Remediation &amp;<br>Special Tire Clean-Ups</h3>
    </div>
    <p>GraniteLoop's core business was derived from our handling of special tire clean up situations. These abandoned or neglected tire piles are not only an environmental but a health concern for the community. We are industry leaders with a large array of fully mobile shredders and ancillary heavy machinery. Our hands-on team is dedicated and driven to handle all special situations that need to be met with a heightened level of precision, care and attention to detail</p>
    <div class="card-arrow"><svg width="18" height="10" viewBox="0 0 18 10"><path d="M0,5 H16 M12,1 L16,5 L12,9" fill="none" stroke="#111" stroke-width="1.8"/></svg></div>
  </article>

  <article class="card" style="left:122px;top:587px">
    <div class="card-head">
      <svg width="44" height="44" viewBox="0 0 44 44"><rect x="3" y="7" width="32" height="28" rx="2" fill="none" stroke="#222" stroke-width="2"/><path d="M3,15 H35 M10,3 V10 M28,3 V10" stroke="#222" stroke-width="2"/><circle cx="33" cy="33" r="9" fill="#fff" stroke="#1f9a3e" stroke-width="2.5"/><path d="M33,28 V33 H37" fill="none" stroke="#1f9a3e" stroke-width="2"/></svg>
      <h3>Scheduling &amp; Billing</h3>
    </div>
    <p>GraniteLoop is here to make your day-to-day easier with a seamless scheduling program. We pride ourselves in prompt tire collections while taking the burdens off our customers with a priority to customer convenience. From scheduled waste tire collections all the way through bespoke, customer-first programs we take the effort off of our customers from dealing with time-consuming scheduling.</p>
    <div class="card-arrow"><svg width="18" height="10" viewBox="0 0 18 10"><path d="M0,5 H16 M12,1 L16,5 L12,9" fill="none" stroke="#111" stroke-width="1.8"/></svg></div>
  </article>

  <article class="card" style="left:591px;top:530px">
    <div class="card-head">
      <svg width="44" height="44" viewBox="0 0 44 44"><circle cx="20" cy="18" r="9" fill="none" stroke="#222" stroke-width="2"/><path d="M6,40 a14,12 0 0 1 28,0" fill="none" stroke="#222" stroke-width="2"/><path d="M9,18 a11,11 0 0 1 22,0" fill="none" stroke="#1f9a3e" stroke-width="2.5"/><rect x="28" y="3" width="14" height="9" rx="2" fill="#1f9a3e"/></svg>
      <h3>First Rate Customer<br>Support &amp; Service</h3>
    </div>
    <p>At GraniteLoop our customer is our priority. We have built a team that shares in our commitment to excellence and shares in our drive to deliver a cutting-edge, courteous experience. GraniteLoop is on a mission to redefine waste tire collection, with stellar customer service at the forefront.We are in this business to build a legacy that embraces our core values to customer focused, environmentally responsible waste tire collection and recycling.</p>
    <div class="card-arrow"><svg width="18" height="10" viewBox="0 0 18 10"><path d="M0,5 H16 M12,1 L16,5 L12,9" fill="none" stroke="#111" stroke-width="1.8"/></svg></div>
  </article>
</section>

<section class="section stats" role="img" aria-label="Dark photo background of a tire tunnel">
  <div class="stat" style="left:113px"><strong>40K</strong><span>customer locations nationwide<br>call us each year to handle their<br>scrap tires day-in and day-out</span></div>
  <div class="stat" style="left:444px"><strong>10M</strong><span>tires diverted from the<br>waste stream each year</span></div>
  <div class="stat" style="left:770px"><strong>884</strong><span>"green" beneficial products<br>produced each year</span></div>
</section>

<section class="section products">
  <h2 class="heading">Products</h2>
  <div class="body-copy">TDF: GraniteLoop seeks to be one of the leading TDF suppliers to the region. This is a product with a wide range of demand from pulp and paper mills, electrical utilities, industrial boilers to cement and asphalt plants our expertly handled tire-derived fuel is being used and receiving high marks for its ever-expanding list of benefits. From driving boiler efficiency to stamping out emissions, GraniteLoop wants to be your TDF supplier offering additional services to include tire pick-up to TDF drop-off we have your back!</div>
  <div class="tile" style="left:450px;top:89px;background:linear-gradient(150deg,#4a4f55,#23272b 60%,#3a8a3a 62%,#2a2e33 75%)" role="img" aria-label="Photo of stacked tires with one green tire"></div>
  <div class="tile" style="left:781px;top:89px;background:linear-gradient(180deg,#7f8a8a 0%,#b7a27a 45%,#2a2a26 70%,#55603a 100%)" role="img" aria-label="Photo of car wheels standing on grass at sunset"></div>
  <div class="tile" style="left:450px;top:314px;background:linear-gradient(180deg,#0c0c0c 0%,#2b2b2b 45%,#111 100%)" role="img" aria-label="Photo of a row of new tire treads"></div>
  <div class="tile" style="left:781px;top:314px;background:linear-gradient(135deg,#2b3946,#4d5d6b 40%,#b98a6a 55%,#1e252c 100%)" role="img" aria-label="Photo of a mechanic's hands fitting a tire"></div>
</section>

<section class="section contact">
  <h2 class="heading">Get In Touch</h2>
  <p class="lead">If you have any questions, just fill in the contact form,<br>and we will be in contact shortly</p>
  <div class="field" style="left:337px;top:242px;width:257px">Company Name:</div>
  <div class="field" style="left:608px;top:242px;width:255px">Email:</div>
  <div class="field" style="left:337px;top:291px;width:257px">Phone:</div>
  <div class="field" style="left:608px;top:291px;width:255px">Address of Business for PickUp:</div>
  <div class="field" style="left:337px;top:341px;width:257px">Number of tires:</div>
  <div class="field" style="left:608px;top:341px;width:255px">Pickup Frequency:</div>
  <div class="field tall" style="left:337px;top:392px;width:526px">Message:</div>
  <div class="btn submit" style="left:530px;top:464px">Submit Now</div>
</section>

<footer class="section site-footer">
  <div class="footer-brand-box">
    <div class="brand" style="position:static;font-size:34px">
      <span class="dot" style="width:22px;height:22px"></span>GraniteLoop
    </div>
  </div>
  <div class="contact-item" style="left:286px">
    <span class="ico"><svg width="14" height="16" viewBox="0 0 14 16"><path d="M7,15 C2,9 1,7 1,6 a6,6 0 0 1 12,0 c0,1 -1,3 -6,9z" fill="#fff"/><circle cx="7" cy="6" r="2" fill="#1f9a3e"/></svg></span>
    <div>Address: Lorem udoa<br>Lore,456 lorems IKSS</div>
  </div>
  <div class="contact-item" style="left:518px">
    <span class="ico"><svg width="14" height="14" viewBox="0 0 14 14"><path d="M3,1 L5,4 L4,6 Q6,9 8,10 L10,9 L13,11 L11,13 Q5,13 1,3 Z" fill="#fff"/></svg></span>
    <div>Phone:<br>555 787 0142</div>
  </div>
  <div class="contact-item" style="left:708px">
    <span class="ico"><svg width="14" height="11" viewBox="0 0 14 11"><rect x="0.5" y="0.5" width="13" height="10" fill="#fff"/><path d="M1,1 L7,6 L13,1" fill="none" stroke="#1f9a3e" stroke-width="1.4"/></svg></span>
    <div>Email:<br>info@graniteloop.example</div>
  </div>
  <p class="copyright">© 2022 All rights reserved. Privacy Policy</p>
</footer>

</body>
</html>
```